MARBLED SPARROW WEB DESIGN PROJECT

We are a brand new company called "Marbled Sparrow" which specialise in one-off Vintage Clothing. We would like somebody to design a web page which will be the sole income for our company. Our main aim is to have an easy searchable website which is user friendly. The key to the website is to target people who do not like the idea of op-shopping but love vintage clothes - this website will be the answer.
Updates

This website will need to be coded to work with Tin Lantern - Please read this before you start. https://help.tinlantern.example/articles/Public/How-do-I-create-custom-template-files-for-my-store

Hi everyone, Just want to make note that the this website is for young people. Just so people a clear I want modern young people dressed in Vintage clothes as this is that reality and what they would like to see. Not people dressed like they are going to a fancy dress party, i.e. dresses like it was that era. Thanks Mirela

Coding

Coded - Design and coding required

```html
<!DOCTYPE html>
<html lang="en">
<head>
<meta charset="utf-8">
<title>Marbled Sparrow — Unique Vintage Fashion and Accessories</title>
<link rel="stylesheet" href="https://fonts.googleapis.com/css2?family=Open+Sans:wght@400;600;700&family=Dosis:wght@400;500;600&family=Kaushan+Script&display=swap">
<style>
:root{
  --teal:#1fc4c8;
  --teal-dark:#17a9ad;
  --red:#e2484d;
  --ink:#333333;
  --ink-soft:#555555;
  --line:#d6d6d6;
  --paper:#ffffff;
  --mist:#ececec;
  --charcoal:#3a3a3a;
  --charcoal-deep:#2b2b2b;
  --hero-bg:#e6e6e6;
}
*{box-sizing:border-box;margin:0;padding:0}
html,body{width:1200px;height:3013px;overflow:hidden}
body{position:relative;background:var(--paper);font-family:"Open Sans",Arial,sans-serif;color:var(--ink)}
.abs{position:absolute}
a{color:inherit;text-decoration:none}

/* utility bar */
.util-bar{left:0;top:0;width:1200px;height:25px;background:var(--mist);font-size:12px;color:var(--ink-soft)}
.util-bar ul{position:absolute;right:40px;top:5px;display:flex;gap:36px;list-style:none}

/* header */
.brand{left:28px;top:50px}
.brand-name{font-weight:600;font-size:40px;color:var(--teal);line-height:1}
.brand-tag{font-size:14px;color:var(--ink);margin-top:10px}
.search{left:648px;top:55px;width:160px;height:30px;border:1px solid var(--line);font-size:11px;color:#777;padding:7px 8px;background:#fafafa;white-space:nowrap;overflow:hidden}
.search-btn{left:806px;top:55px;width:30px;height:30px;background:var(--teal)}
.btn-signup,.btn-login{top:56px;height:28px;width:84px;color:#fff;font-size:12px;font-weight:700;text-align:center;line-height:28px}
.btn-signup{left:851px;background:var(--red)}
.btn-login{left:951px;background:var(--charcoal)}
.help-links{left:1090px;top:52px;font-size:14px;line-height:22px;text-align:center}
.ship-note{left:816px;top:114px;font-size:13px;font-weight:700;color:var(--ink);display:flex;align-items:center;gap:8px;white-space:nowrap}

/* gender switch */
.gender-bar{left:0;top:163px;width:1200px;height:63px;border-top:1px solid var(--line);border-bottom:1px solid var(--line)}
.gender-bar .divider{left:602px;top:0;width:1px;height:63px;background:var(--line)}
.gender{top:0;height:63px;width:602px;display:flex;align-items:center;justify-content:center;gap:10px;font-family:"Dosis",sans-serif;font-size:32px;font-weight:500;letter-spacing:1px}
.gender.women{left:0;color:var(--ink)}
.gender.men{left:602px;color:var(--red)}
.gender.women .underline{position:absolute;left:140px;right:140px;bottom:0;height:4px;background:var(--ink)}

/* category nav */
.cat-nav{left:0;top:231px;width:1200px;height:70px;border-bottom:1px solid var(--line);display:flex}
.cat-nav a{display:flex;align-items:center;justify-content:center;font-family:"Dosis",sans-serif;font-size:15px;font-weight:600;white-space:nowrap;border-right:1px solid var(--line);text-transform:uppercase}
.cat-nav a.w-s{width:168px}
.cat-nav a.w-l{width:264px}
.cat-nav a.active{box-shadow:inset 0 -3px 0 var(--ink)}

/* hero */
.hero{left:0;top:301px;width:1200px;height:572px;background:var(--hero-bg);overflow:hidden}
.hero-photo{position:absolute;top:0;height:572px}
.hero-photo.left{left:0;width:420px;background:linear-gradient(160deg,#d9d9d9,#f0a79d 55%,#e88378)}
.hero-photo.right{left:840px;width:360px;background:linear-gradient(200deg,#dcdcdc,#2c3350 60%,#1f2540)}
.hero-photo.center{left:300px;width:600px;clip-path:polygon(26% 0,100% 0,77% 100%,45% 100%);background:linear-gradient(180deg,#e7c58d,#c99a6a 45%,#a0622f 80%,#6d4a3c)}
.hero-arrow{position:absolute;top:236px}
.hero-title{left:340px;top:462px;width:520px;text-align:center;font-family:"Dosis",sans-serif;font-size:50px;font-weight:500;line-height:64px;color:#fff;letter-spacing:1px;text-transform:uppercase;white-space:nowrap}
.hero-dots{left:556px;top:838px;display:flex;gap:18px}
.hero-dots span{width:16px;height:16px;border-radius:50%;background:var(--teal-dark)}

/* dropdown */
.dropdown{left:0;top:319px;width:259px;background:var(--teal);list-style:none;padding-bottom:8px}
.dropdown li{font-family:"Dosis",sans-serif;font-size:15px;font-weight:600;color:#fff;padding:0 40px;height:32px;line-height:32px;text-transform:uppercase}
.dropdown li.current{background:var(--charcoal-deep)}

/* tabs */
.tabs{left:0;top:896px;width:1200px;height:50px;border-bottom:4px solid var(--ink)}
.tab{position:absolute;top:0;height:46px;line-height:46px;font-family:"Dosis",sans-serif;font-size:22px;font-weight:500;text-transform:uppercase;text-align:center}
.tab.featured{left:0;width:270px;background:var(--ink);color:#fff}
.tab.popular{left:276px;width:130px;background:var(--mist)}
.tab.bestsellers{left:410px;width:150px;background:var(--mist)}
.tab-arrows{right:14px;top:8px;display:flex;gap:6px}
.tab-arrows span{width:32px;height:32px;border:1px solid var(--line);background:#f6f6f6;display:flex;align-items:center;justify-content:center}

/* product cards */
.product{width:196px;height:246px;border:1px solid var(--line);background:#f2f2f2}
.product .photo{position:absolute;left:0;top:0;width:194px;height:208px}
.product .cart{position:absolute;right:0;top:0;width:38px;height:38px;background:#777;display:flex;align-items:center;justify-content:center}
.product .price{position:absolute;left:18px;top:120px;width:50px;height:50px;border-radius:50%;background:var(--teal);color:#fff;font-weight:700;font-size:16px;text-align:center;line-height:50px}
.product .label{position:absolute;left:0;bottom:0;width:194px;height:36px;background:var(--teal);color:#fff;font-family:"Dosis",sans-serif;font-size:17px;font-weight:500;text-align:center;line-height:36px;text-transform:uppercase;white-space:nowrap}
.product.hot{border-color:var(--red)}
.product.hot .cart,.product.hot .price,.product.hot .label{background:var(--red)}
.ph-black{background:radial-gradient(ellipse 30% 60% at 50% 55%,#4a4a4a,rgba(74,74,74,0) 70%),linear-gradient(180deg,#f3f3f3,#e4e4e4)}
.ph-pink{background:radial-gradient(ellipse 30% 60% at 50% 55%,#ec7f93,rgba(236,127,147,0) 70%),linear-gradient(180deg,#f5eef0,#f0e4e6)}
.ph-dots{background:radial-gradient(ellipse 30% 60% at 50% 55%,#2e3552,rgba(46,53,82,0) 70%),linear-gradient(180deg,#f2f2f4,#e2e3ea)}
.ph-aqua{background:radial-gradient(ellipse 30% 60% at 50% 55%,#5fe0dc,rgba(95,224,220,0) 70%),linear-gradient(180deg,#f1f5f5,#e4f1f1)}

/* promo band */
.promo-band{left:0;top:1539px;width:1200px;height:461px;background:linear-gradient(90deg,#2e2e2e,#4a4a4a 50%,#2a2a2a)}
.promo-card{top:1581px;height:377px;background:#fff}
.promo-card .visual{position:absolute;left:0;top:0;width:100%;height:245px}
.promo-card .heading{position:absolute;left:22px;top:6px;font-family:"Kaushan Script",cursive;font-size:54px;color:var(--teal);line-height:1.2}
.promo-card .heading small{font-family:"Dosis",sans-serif;font-size:24px;color:var(--red);text-transform:uppercase;margin-left:6px}
.promo-card p{position:absolute;left:30px;top:260px;right:30px;font-size:13px;line-height:17px;color:var(--ink)}
.promo-card .more{position:absolute;left:30px;top:332px;width:112px;height:30px;background:var(--teal);color:#fff;font-size:13px;font-weight:600;text-align:center;line-height:30px}
.vip{left:926px;top:1581px;width:241px;height:365px;background:#cfd1d3}
.vip .visual{position:absolute;left:0;top:0;width:241px;height:183px;background:linear-gradient(160deg,#5a5a5a,#2b2b2b)}
.vip .offer{position:absolute;left:10px;top:18px;font-family:"Dosis",sans-serif;font-size:27px;color:#fff;line-height:38px;white-space:nowrap}
.vip .offer em{font-family:"Kaushan Script",cursive;font-style:normal;color:var(--teal)}
.vip p{position:absolute;left:12px;top:192px;right:12px;font-size:13px;line-height:17px}
.vip .field{position:absolute;left:12px;width:217px;height:32px;background:#9a9da1;color:#fff;font-size:13px;padding:7px 10px}
.vip .join{position:absolute;left:107px;top:320px;width:122px;height:30px;background:var(--teal);color:#fff;font-size:13px;font-weight:600;text-align:center;line-height:30px}

/* manifesto */
.manifesto{left:0;top:2000px;width:1200px;height:272px;background:var(--mist);text-align:center;font-family:"Dosis",sans-serif;font-size:36px;color:var(--ink);font-weight:500}
.manifesto p{position:absolute;left:0;width:1200px}
.manifesto .script{font-family:"Kaushan Script",cursive;color:var(--red);font-size:32px}

/* newsletter */
.newsletter{left:0;top:2272px;width:1200px;height:276px;background:linear-gradient(90deg,#6b6b6b,#555 60%,#4a4a4a)}
.newsletter .visual{position:absolute;left:0;top:0;width:452px;height:276px;background:linear-gradient(120deg,#9a8f88,#c7a88d 45%,#6f6a66)}
.newsletter h2{position:absolute;left:452px;width:748px;top:22px;text-align:center;font-family:"Kaushan Script",cursive;font-weight:400;font-size:36px;color:#fff}
.newsletter h3{position:absolute;left:452px;width:748px;top:80px;text-align:center;font-family:"Dosis",sans-serif;font-weight:500;font-size:36px;color:#fff}
.newsletter .email{position:absolute;left:657px;top:152px;width:325px;height:40px;background:#2c2c2c;color:#fff;font-size:14px;text-align:center;line-height:40px}
.newsletter .subscribe{position:absolute;left:761px;top:207px;width:118px;height:34px;background:var(--teal);color:#fff;font-size:14px;font-weight:600;text-align:center;line-height:34px;text-transform:uppercase}

/* social strip */
.social{left:0;top:2548px;width:1200px;height:63px;background:#e2e2e2}
.social-item{position:absolute;top:14px;display:flex;align-items:center;gap:8px;font-size:14px;font-weight:600;color:#6b6b6b;transform:translateX(-50%)}
.social-item i{width:34px;height:34px;border-radius:50%;background:#8a8a8a;display:block}

/* footer */
.footer{left:0;top:2611px;width:1200px;height:326px;background:var(--charcoal);color:#fff}
.footer h4{position:absolute;top:40px;font-size:20px;font-weight:700}
.footer ul{position:absolute;top:86px;list-style:none;font-size:16px;line-height:33px}
.footer li::before{content:"›";margin-right:18px;font-weight:700}
.footer .cols2 li span{display:inline-block;width:172px}
.legal{left:0;top:2937px;width:1200px;height:76px;background:#fff;font-size:16px;font-weight:600;color:var(--ink)}
.legal .copy{position:absolute;left:70px;top:26px}
.pay{position:absolute;top:22px;height:34px;display:flex;align-items:center;font-size:18px;font-weight:700;color:#555}
.badge{position:absolute;top:24px;height:30px;background:#bdbdbd;border-radius:4px}
</style>
</head>
<body>

<div class="abs util-bar"><ul><li><a href="#">View Cart</a></li><li><a href="#">Wish List</a></li><li><a href="#">Help</a></li></ul></div>

<header>
  <div class="abs brand">
    <div class="brand-name">Marbled Sparrow</div>
    <div class="brand-tag">Unique Vintage Fashion and Accessori</div>
  </div>
  <div class="abs search">Search one off vintage items</div>
  <div class="abs search-btn"><svg width="30" height="30" viewBox="0 0 30 30"><circle cx="13" cy="13" r="6" fill="none" stroke="#fff" stroke-width="2"/><line x1="17.5" y1="17.5" x2="22" y2="22" stroke="#fff" stroke-width="2.5"/></svg></div>
  <a class="abs btn-signup" href="#">SIGN UP</a>
  <a class="abs btn-login" href="#">LOG IN</a>
  <div class="abs help-links">STYLE TIPS<br>FAQ</div>
  <div class="abs ship-note"><svg width="38" height="22" viewBox="0 0 38 22"><rect x="0" y="2" width="22" height="13" fill="var(--teal)"/><path d="M22 6h8l6 5v4H22z" fill="var(--teal)"/><circle cx="7" cy="17" r="3.5" fill="#333"/><circle cx="29" cy="17" r="3.5" fill="#333"/></svg>ORDERS OVER $100 WILL RECEVIE FREE SHIPPING!</div>
</header>

<nav class="abs gender-bar">
  <a class="abs gender women" href="#">WOMEN <svg width="28" height="36" viewBox="0 0 28 36"><path d="M10 2h8l-1 8 9 22H2l9-22z" fill="#1e4a48"/></svg><span class="underline"></span></a>
  <span class="abs divider"></span>
  <a class="abs gender men" href="#">MEN <svg width="36" height="32" viewBox="0 0 36 32"><path d="M12 2h12l10 7-4 6-4-2v17H10V13l-4 2-4-6z" fill="var(--red)"/></svg></a>
</nav>

<nav class="abs cat-nav">
  <a class="w-s active" href="#">Vintage Clothing</a>
  <a class="w-s" href="#">Vintage Shoes</a>
  <a class="w-l" href="#">Old-Fashioned Assessories</a>
  <a class="w-s" href="#">Vintage Clothing</a>
  <a class="w-s" href="#">Vintage Shoes</a>
  <a class="w-l" href="#" style="border-right:0">Old-Fashioned Assessories</a>
</nav>

<section class="abs hero">
  <div class="hero-photo left" role="img" aria-label="Model in a coral belted vintage dress"></div>
  <div class="hero-photo right" role="img" aria-label="Model in a navy polka dot strapless dress"></div>
  <div class="hero-photo center" role="img" aria-label="Smiling model in a patterned boho jacket with bangles"></div>
  <svg class="hero-arrow" style="left:24px" width="30" height="80" viewBox="0 0 30 80"><polyline points="26,4 4,40 26,76" fill="none" stroke="#fff" stroke-width="3"/></svg>
  <svg class="hero-arrow" style="left:1146px" width="30" height="80" viewBox="0 0 30 80"><polyline points="4,4 26,40 4,76" fill="none" stroke="#fff" stroke-width="3"/></svg>
</section>
<h1 class="abs hero-title">A Diverse Varity<br>of Glamorous High<br>Quality Cloths</h1>
<div class="abs hero-dots"><span></span><span></span><span></span></div>

<ul class="abs dropdown">
  <li class="current">Dresses</li>
  <li>Shirts &amp; T Shirts</li>
  <li>Shorts</li>
  <li>Trousers, Pants &amp; Jeans</li>
  <li>Jumpsuits &amp; Playsuits</li>
</ul>

<div class="abs tabs">
  <div class="tab featured">Featured Products</div>
  <div class="tab popular">Popular</div>
  <div class="tab bestsellers">Best Sellers</div>
  <div class="abs tab-arrows">
    <span><svg width="12" height="16" viewBox="0 0 12 16"><polyline points="9,2 3,8 9,14" fill="none" stroke="#999" stroke-width="2"/></svg></span>
    <span><svg width="12" height="16" viewBox="0 0 12 16"><polyline points="3,2 9,8 3,14" fill="none" stroke="#999" stroke-width="2"/></svg></span>
  </div>
</div>

<!-- product grid: row 1 -->
<div class="abs product" style="left:35px;top:976px"><div class="photo ph-black" role="img" aria-label="Model in a black 1950s party dress"></div><div class="cart"><svg width="20" height="18" viewBox="0 0 20 18"><path d="M1 2h3l2 9h10l2-7H6" fill="none" stroke="#fff" stroke-width="1.8"/><circle cx="8" cy="15" r="1.6" fill="#fff"/><circle cx="15" cy="15" r="1.6" fill="#fff"/></svg></div><div class="price">$25</div><div class="label">1950s Party Dress</div></div>
<div class="abs product" style="left:266px;top:976px"><div class="photo ph-pink" role="img" aria-label="Model in a pink double breasted coat"></div><div class="cart"><svg width="20" height="18" viewBox="0 0 20 18"><path d="M1 2h3l2 9h10l2-7H6" fill="none" stroke="#fff" stroke-width="1.8"/><circle cx="8" cy="15" r="1.6" fill="#fff"/><circle cx="15" cy="15" r="1.6" fill="#fff"/></svg></div><div class="price">$30</div><div class="label">Double Breasted Coat</div></div>
<div class="abs product hot" style="left:502px;top:976px"><div class="photo ph-dots" role="img" aria-label="Model in a navy polka dot 1960s dress"></div><div class="cart"><svg width="20" height="18" viewBox="0 0 20 18"><path d="M1 2h3l2 9h10l2-7H6" fill="none" stroke="#fff" stroke-width="1.8"/><circle cx="8" cy="15" r="1.6" fill="#fff"/><circle cx="15" cy="15" r="1.6" fill="#fff"/></svg></div><div class="price">$25</div><div class="label">1960s Hippy Dress</div></div>
<div class="abs product" style="left:738px;top:976px"><div class="photo ph-pink" role="img" aria-label="Model in a pink belted 1980s outfit"></div><div class="cart"><svg width="20" height="18" viewBox="0 0 20 18"><path d="M1 2h3l2 9h10l2-7H6" fill="none" stroke="#fff" stroke-width="1.8"/><circle cx="8" cy="15" r="1.6" fill="#fff"/><circle cx="15" cy="15" r="1.6" fill="#fff"/></svg></div><div class="price">$30</div><div class="label">1980s High Pant</div></div>
<div class="abs product" style="left:971px;top:976px"><div class="photo ph-aqua" role="img" aria-label="Model in an aqua double breasted coat"></div><div class="cart"><svg width="20" height="18" viewBox="0 0 20 18"><path d="M1 2h3l2 9h10l2-7H6" fill="none" stroke="#fff" stroke-width="1.8"/><circle cx="8" cy="15" r="1.6" fill="#fff"/><circle cx="15" cy="15" r="1.6" fill="#fff"/></svg></div><div class="price">$30</div><div class="label">Double Breasted Coat</div></div>

<!-- product grid: row 2 -->
<div class="abs product" style="left:35px;top:1260px"><div class="photo ph-black" role="img" aria-label="Model in a black 1950s party dress"></div><div class="cart"><svg width="20" height="18" viewBox="0 0 20 18"><path d="M1 2h3l2 9h10l2-7H6" fill="none" stroke="#fff" stroke-width="1.8"/><circle cx="8" cy="15" r="1.6" fill="#fff"/><circle cx="15" cy="15" r="1.6" fill="#fff"/></svg></div><div class="price">$25</div><div class="label">1950s Party Dress</div></div>
<div class="abs product" style="left:266px;top:1260px"><div class="photo ph-pink" role="img" aria-label="Model in a pink double breasted coat"></div><div class="cart"><svg width="20" height="18" viewBox="0 0 20 18"><path d="M1 2h3l2 9h10l2-7H6" fill="none" stroke="#fff" stroke-width="1.8"/><circle cx="8" cy="15" r="1.6" fill="#fff"/><circle cx="15" cy="15" r="1.6" fill="#fff"/></svg></div><div class="price">$30</div><div class="label">Double Breasted Coat</div></div>
<div class="abs product" style="left:502px;top:1260px"><div class="photo ph-dots" role="img" aria-label="Model in a navy polka dot 1960s dress"></div><div class="cart"><svg width="20" height="18" viewBox="0 0 20 18"><path d="M1 2h3l2 9h10l2-7H6" fill="none" stroke="#fff" stroke-width="1.8"/><circle cx="8" cy="15" r="1.6" fill="#fff"/><circle cx="15" cy="15" r="1.6" fill="#fff"/></svg></div><div class="price">$25</div><div class="label">1960s Hippy Dress</div></div>
<div class="abs product" style="left:738px;top:1260px"><div class="photo ph-pink" role="img" aria-label="Model in a pink belted 1980s outfit"></div><div class="cart"><svg width="20" height="18" viewBox="0 0 20 18"><path d="M1 2h3l2 9h10l2-7H6" fill="none" stroke="#fff" stroke-width="1.8"/><circle cx="8" cy="15" r="1.6" fill="#fff"/><circle cx="15" cy="15" r="1.6" fill="#fff"/></svg></div><div class="price">$30</div><div class="label">1980s High Pant</div></div>
<div class="abs product" style="left:971px;top:1260px"><div class="photo ph-aqua" role="img" aria-label="Model in an aqua double breasted coat"></div><div class="cart"><svg width="20" height="18" viewBox="0 0 20 18"><path d="M1 2h3l2 9h10l2-7H6" fill="none" stroke="#fff" stroke-width="1.8"/><circle cx="8" cy="15" r="1.6" fill="#fff"/><circle cx="15" cy="15" r="1.6" fill="#fff"/></svg></div><div class="price">$30</div><div class="label">Double Breasted Coat</div></div>

<section class="abs promo-band" role="img" aria-label="Dimmed background of racks of vintage clothing"></section>
<article class="abs promo-card" style="left:38px;width:396px">
  <div class="visual" role="img" aria-label="Young woman in a vintage top seated on a wicker chair" style="background:linear-gradient(135deg,#8aa3ad,#6c6f63 50%,#b59a7c)"></div>
  <div class="heading">Style<small>Tips</small></div>
  <p>Lorem ipsum dolor sit amet conse ctetur adipisicing elit, tempor incididunt ut labore et dolore magna aliqua. quis nostrud exercitation ullamco laboris nisi ut.</p>
  <a class="more" href="#">MORE INFO</a>
</article>
<article class="abs promo-card" style="left:477px;width:399px">
  <div class="visual" role="img" aria-label="Young man in a vintage jacket seated outdoors" style="background:linear-gradient(135deg,#5c5a55,#2f2d2b 55%,#7c7468)"></div>
  <div class="heading">Shop<small>Era</small></div>
  <p>Lorem ipsum dolor sit amet conse ctetur adipisicing elit, tempor incididunt ut labore et dolore magna aliqua. quis nostrud exercitation ullamco laboris nisi ut.</p>
  <a class="more" href="#">MORE INFO</a>
</article>
<aside class="abs vip">
  <div class="visual" role="img" aria-label="Dark portrait backdrop"></div>
  <div class="offer"><em>Join</em> OUR VIP CLUB<br>&amp; RECEIVE<br><em>5%</em> OFF <em>every order</em></div>
  <p>Lorem ipsum dolor sit amet conse ctetur adipisicing elit, tempor incididunt ut labore et.</p>
  <div class="field" style="top:242px">Name</div>
  <div class="field" style="top:280px">Email Address</div>
  <a class="join" href="#">JOIN NOW</a>
</aside>

<section class="abs manifesto">
  <p style="top:42px"><span class="script">Marbled Sparrow</span> is all about being different.</p>
  <p style="top:117px">That's way all of our <span class="script">clothes are unique,</span></p>
  <p style="top:190px">so you can be <span class="script">dazzling</span> differentt</p>
</section>

<section class="abs newsletter">
  <div class="visual" role="img" aria-label="Young woman shopping online holding a card at a laptop"></div>
  <h2>Become part of our community</h2>
  <h3>Sign up to our newsletter</h3>
  <div class="email">Email Address</div>
  <a class="subscribe" href="#">Subscribe</a>
</section>

<nav class="abs social">
  <a class="social-item" style="left:133px" href="#"><i></i>Corkboard</a>
  <a class="social-item" style="left:434px" href="#"><i></i>Journal</a>
  <a class="social-item" style="left:766px" href="#"><i></i>Friendnet</a>
  <a class="social-item" style="left:1042px" href="#"><i></i>Snapframe</a>
</nav>

<footer class="abs footer">
  <h4 style="left:60px">Marbled Sparrow</h4>
  <ul style="left:64px"><li>About Us</li><li>Terms of use</li><li>Privacy Policy</li><li>Press</li></ul>
  <h4 style="left:467px">Connect with Us</h4>
  <ul style="left:471px"><li>Contact us</li><li>My Account</li><li>Style Tips</li><li>FAQ</li><li>Shipping</li><li>Track your order</li><li>Size chart</li></ul>
  <h4 style="left:856px">Shop by Popular Categories</h4>
  <ul class="cols2" style="left:860px"><li><span>Men</span>50s</li><li><span>Women</span>60s</li><li><span>Accessories</span>70s</li><li><span>Bags</span>80s</li><li><span>Shoes</span>90s</li></ul>
</footer>

<div class="abs legal">
  <div class="copy">© Marbled Sparrow. All Prices are in AUD.</div>
  <div class="badge" style="left:624px;width:116px"></div>
  <div class="badge" style="left:766px;width:76px"></div>
  <div class="pay" style="left:872px">PayBridge</div>
  <div class="pay" style="left:985px">Vista</div>
  <div class="pay" style="left:1052px">Meridian</div>
</div>

</body>
</html>
```